Etiketten-Design für nachhaltige Rasur- & Pflegeprodukte
> Wir suchen Verpackung und Etiketten für eine Marke für nachhaltige Rasur- & Pflegeprodukte.
Habedere liebe Designer,
„Habedere“ sagt man bei uns in Bayern, es bedeutet Hallo oder auf Wiedersehen, je nach Gelegenheit. In diesem Fall: Hallo.
Vielleicht kennst du uns schon, wir sind greenpines, wir betreiben einen kleinen Shop für Bartpflege & Rasur unter greenpines-shop.de und wir versuchen uns nun an einem neuen Thema: nachhaltige Rasur- & Pflegeprodukte für Frauen.
Das machen wir unter dem Namen „Sanft“.
Weil die Frage schon oft aufkam: Jawohl, wir haben uns dafür die Beine und die Achseln mit einem Rasierhobel rasiert.
> Zielgruppe.
Wir arbeiten an einer neuen Pflegelinie für Frauen, die sich vorwiegend mit der Rasur und den dazugehörigen Pflegeprodukten beschäftigt. Die Zielgruppe sind vor allem online-affine Frauen aus Deutschland, Österreich und der Schweiz, aber sicher auch europaweit im Alter von 21-45.
> Aufgabenstellung.
Wir sind auf der Suche nach einem Konzept für unsere Produktverpackungen bzw. Etiketten. Bei den Pflegeprodukten verzichten wir bewusst auf eine Umverpackung.
Konkret geplant sind ein Rasierhobel, dafür haben wir eine schöne Umverpackung. Außerdem starten wir mit Rasieröl, Rasierseife und einem After Shave Balsam. Es werden später noch andere Artikel dazukommen, eine Deocreme zum Beispiel.
Rasieröl, Rasiercreme und After Shave Balsam duften nach Orangen, es werden zwei oder drei weitere Duftrichtungen folgen, die eine wird beispielsweise nach Beeren duften, die andere nach Pfirsich und Mango – bitte beachte das bei der Erstellung des Konzeptes, die Unterschiede sollten später auf den ersten Blick erkennbar sein.
Zurück zum Thema Orange: Wir würden den Duft als leicht herben Zitrusduft bezeichnen.
> Die Maße.
• Umverpackung Rasierhobel, weißer Karton (165x90x40mm)
• Rasieröl 30ml (Etikett: 100x46mm)
• Rasiercreme 60ml (Etikett: 156x32mm)
• After Shave Balsam 60ml (Etikett: 156x32mm)
> Zwingend erforderliche Angaben.
Da es sich um Kosmetikprodukte handelt, sind einige Angaben auf dem Label zwingend erforderlich, beispielhaft sollen die folgenden Infos als Platzhalter dienen.
• Hergestellt für Tobias Kranzler e.K. von greenpines, Lindenhofweg 27, 83109 Rosenheim
• Ingredients: Aqua, Stearic Acid, Cocos Nucifera oil, Glycerin, Potassium Hydroxide, Litsea Cubeba oil, (and) Citrus Sinensis Peel oil, Orbignya Oleifera oil, Sodium Hydroxide, Macadamia ternifolia oil, Talc, Kaolin, Citric Acid, Simmondsia chinensis oil, Maris sal, C.I. 77892 (and) Rad Clay, Citral, Limonene, Linalool, Geraniol
• Platz für einen Barcode
• Rasieröl sind 30ml / 1.01 FL.OZ. ODER Creme & Balsam jeweils 60ml / 2.03 FL. OZ.
Wir haben ein Bild der aktuellen Gefäße beigefügt, es kann aber durchaus sein, dass wir uns noch umen..

```html
<!DOCTYPE html>
<html lang="de">
<head>
<meta charset="utf-8">
<title>Miravel – After Shave Balsam Etiketten</title>
<link rel="stylesheet" href="https://fonts.googleapis.com/css2?family=Didact+Gothic&family=Federo&family=Noto+Sans:wght@400;500&display=swap">
<style>
  :root {
    --page: #dfe0db;
    --paper: #e8e5ea;
    --brand: #5f8f85;
    --ink-green: #2f4a3f;
    --ink: #2b2b2b;
    --berry: #7a4a72;
    --berry-soft: #d9c3d8;
    --berry-mid: #a07a9c;
    --mango: #e6ac3c;
    --mango-soft: #efd9b8;
    --orange: #e69a2e;
    --orange-soft: #f0d2b0;
    --peach: #dca06a;
    --peach-soft: #efd3c0;
    --peach-mid: #e6bb94;
  }
  * { box-sizing: border-box; margin: 0; padding: 0; }
  html, body { width: 667px; height: 1200px; overflow: hidden; }
  body {
    background: var(--page);
    font-family: "Noto Sans", sans-serif;
    color: var(--ink);
  }
  .sheet {
    display: grid;
    grid-template-columns: 310px 310px;
    grid-template-rows: repeat(4, 250px);
    column-gap: 15px;
    row-gap: 38px;
    padding: 43px 16px;
  }
  .label {
    position: relative;
    overflow: hidden;
    background: var(--paper);
    box-shadow: 0 1px 3px rgba(0,0,0,.12);
  }
  .label.berry  { --accent: var(--berry);  --soft: var(--berry-soft);  --mid: var(--berry-mid); }
  .label.mango  { --accent: var(--mango);  --soft: var(--mango-soft);  --mid: var(--mango); }
  .label.orange { --accent: var(--orange); --soft: var(--orange-soft); --mid: var(--orange); }
  .label.peach  { --accent: var(--peach);  --soft: var(--peach-soft);  --mid: var(--peach-mid); }
  .decor { position: absolute; inset: 0; width: 100%; height: 100%; }
  .decor .accent { fill: var(--accent); }
  .decor .soft { fill: var(--soft); }
  .decor .mid { fill: var(--mid); }
  .content {
    position: relative;
    height: 100%;
    display: flex;
    flex-direction: column;
    align-items: center;
    text-align: center;
  }
  .brand {
    margin-top: 42px;
    font-family: "Didact Gothic", sans-serif;
    font-weight: 400;
    font-size: 20px;
    letter-spacing: 1px;
    color: var(--brand);
  }
  .product {
    font-family: "Didact Gothic", sans-serif;
    font-weight: 400;
    color: var(--ink-green);
    font-size: 21px;
    letter-spacing: .3px;
  }
  .front .product { margin-top: 26px; }
  .scent {
    font-family: "Federo", sans-serif;
    color: var(--accent);
    font-size: 27px;
    letter-spacing: 1px;
    margin-top: 10px;
  }
  .volume { font-size: 8px; letter-spacing: .5px; margin-top: auto; margin-bottom: 28px; }
  .back .product { margin-top: 26px; font-size: 17px; }
  .back .scent { font-size: 17px; margin-top: 2px; }
  .maker { font-size: 7.4px; line-height: 1.35; margin-top: 8px; }
  .ingredients {
    align-self: stretch;
    text-align: left;
    padding: 0 26px 0 22px;
    font-size: 6.2px;
    line-height: 1.4;
    margin-top: 8px;
  }
  .ingredients strong { display: block; font-weight: 500; margin-bottom: 2px; }
  .back .volume { font-size: 10px; margin: 8px 0 26px 60px; align-self: flex-start; }
</style>
</head>
<body>
<main class="sheet">

  <section class="label berry front">
    <svg class="decor" viewBox="0 0 310 250">
      <circle class="mid" cx="4" cy="38" r="44" role="img" aria-label="Blattzeichnung auf farbiger Scheibe"/>
      <circle class="soft" cx="0" cy="150" r="40"/>
      <rect class="mid" x="0" y="182" width="34" height="26"/>
      <polygon class="soft" points="215,0 310,0 310,6 225,22"/>
      <rect class="mid" x="289" y="24" width="8" height="8"/>
      <rect class="mid" x="289" y="38" width="8" height="8"/>
      <rect class="accent" x="288" y="100" width="22" height="22"/>
      <circle class="soft" cx="296" cy="168" r="46" role="img" aria-label="Blattzeichnung auf farbiger Scheibe"/>
      <rect class="soft" x="248" y="215" width="36" height="18"/>
    </svg>
    <div class="content">
      <p class="brand">Miravel</p>
      <h2 class="product">After Shave Balsam</h2>
      <p class="scent">Beeren</p>
      <p class="volume">60 ml/2.03 FL.OZ.</p>
    </div>
  </section>
  <section class="label berry back">
    <svg class="decor" viewBox="0 0 310 250">
      <circle class="mid" cx="4" cy="30" r="36" role="img" aria-label="Blattzeichnung auf farbiger Scheibe"/>
      <circle class="soft" cx="0" cy="160" r="30"/>
      <rect class="mid" x="0" y="200" width="30" height="22"/>
      <polygon class="soft" points="210,0 310,0 310,6 222,20"/>
      <rect class="mid" x="293" y="20" width="7" height="7"/>
      <rect class="mid" x="293" y="32" width="7" height="7"/>
      <rect class="accent" x="294" y="120" width="16" height="20"/>
      <circle class="soft" cx="304" cy="196" r="32" role="img" aria-label="Blattzeichnung auf farbiger Scheibe"/>
      <rect class="soft" x="200" y="222" width="34" height="14"/>
    </svg>
    <div class="content">
      <h2 class="product">After Shave Balsam</h2>
      <p class="scent">Beeren</p>
      <p class="maker">Hergestellt für Tobias Kranzler e.K.<br>von greenpines, Lindenhofweg 27, 83109 Rosenheim.</p>
      <p class="ingredients"><strong>Ingredients:</strong>Aqua, Stearic Acid, Cocos Nucifera oil, Glycerin, Potassium Hydroxide, Litsea Cubeba oil, (and) Citrus Sinensis Peel oil, Orbignya Oleifera oil, Sodium Hydroxide, Macadamia ternifolia oil, Talc, Kaolin, Citric Acid, Simmondsia chinensis oil, Maris sal, C.I. 77892 (and) Rad Clay, Citral, Limonene, Linalool, Geraniol.</p>
      <p class="volume">60 ml/2.03 FL.OZ.</p>
    </div>
  </section>

  <section class="label mango front">
    <svg class="decor" viewBox="0 0 310 250">
      <circle class="accent" cx="4" cy="38" r="44" role="img" aria-label="Blattzeichnung auf farbiger Scheibe"/>
      <circle class="soft" cx="0" cy="150" r="40"/>
      <rect class="accent" x="0" y="182" width="34" height="26"/>
      <polygon class="soft" points="215,0 310,0 310,6 225,22"/>
      <rect class="accent" x="289" y="24" width="8" height="8"/>
      <rect class="accent" x="289" y="38" width="8" height="8"/>
      <rect class="accent" x="288" y="100" width="22" height="22"/>
      <circle class="soft" cx="296" cy="168" r="46" role="img" aria-label="Blattzeichnung auf farbiger Scheibe"/>
      <rect class="accent" x="248" y="215" width="36" height="18"/>
    </svg>
    <div class="content">
      <p class="brand">Miravel</p>
      <h2 class="product">After Shave Balsam</h2>
      <p class="scent">Mango</p>
      <p class="volume">60 ml/2.03 FL.OZ.</p>
    </div>
  </section>
  <section class="label mango back">
    <svg class="decor" viewBox="0 0 310 250">
      <circle class="accent" cx="4" cy="30" r="36" role="img" aria-label="Blattzeichnung auf farbiger Scheibe"/>
      <circle class="soft" cx="0" cy="160" r="30"/>
      <rect class="accent" x="0" y="200" width="30" height="22"/>
      <polygon class="soft" points="210,0 310,0 310,6 222,20"/>
      <rect class="accent" x="293" y="20" width="7" height="7"/>
      <rect class="accent" x="293" y="32" width="7" height="7"/>
      <rect class="accent" x="294" y="120" width="16" height="20"/>
      <circle class="soft" cx="304" cy="196" r="32" role="img" aria-label="Blattzeichnung auf farbiger Scheibe"/>
      <rect class="accent" x="200" y="222" width="34" height="14"/>
    </svg>
    <div class="content">
      <h2 class="product">After Shave Balsam</h2>
      <p class="scent">Mango</p>
      <p class="maker">Hergestellt für Tobias Kranzler e.K.<br>von greenpines, Lindenhofweg 27, 83109 Rosenheim.</p>
      <p class="ingredients"><strong>Ingredients:</strong>Aqua, Stearic Acid, Cocos Nucifera oil, Glycerin, Potassium Hydroxide, Litsea Cubeba oil, (and) Citrus Sinensis Peel oil, Orbignya Oleifera oil, Sodium Hydroxide, Macadamia ternifolia oil, Talc, Kaolin, Citric Acid, Simmondsia chinensis oil, Maris sal, C.I. 77892 (and) Rad Clay, Citral, Limonene, Linalool, Geraniol.</p>
      <p class="volume">60 ml/2.03 FL.OZ.</p>
    </div>
  </section>

  <section class="label orange front">
    <svg class="decor" viewBox="0 0 310 250">
      <circle class="accent" cx="4" cy="38" r="44" role="img" aria-label="Blattzeichnung auf farbiger Scheibe"/>
      <circle class="soft" cx="0" cy="150" r="40"/>
      <rect class="accent" x="0" y="182" width="34" height="26"/>
      <polygon class="soft" points="215,0 310,0 310,6 225,22"/>
      <rect class="accent" x="289" y="24" width="8" height="8"/>
      <rect class="accent" x="289" y="38" width="8" height="8"/>
      <rect class="accent" x="288" y="100" width="22" height="22"/>
      <circle class="soft" cx="296" cy="168" r="46" role="img" aria-label="Blattzeichnung auf farbiger Scheibe"/>
      <rect class="accent" x="248" y="215" width="36" height="18"/>
    </svg>
    <div class="content">
      <p class="brand">Miravel</p>
      <h2 class="product">After Shave Balsam</h2>
      <p class="scent">Orange</p>
      <p class="volume">60 ml/2.03 FL.OZ.</p>
    </div>
  </section>
  <section class="label orange back">
    <svg class="decor" viewBox="0 0 310 250">
      <circle class="accent" cx="4" cy="30" r="36" role="img" aria-label="Blattzeichnung auf farbiger Scheibe"/>
      <circle class="soft" cx="0" cy="160" r="30"/>
      <rect class="accent" x="0" y="200" width="30" height="22"/>
      <polygon class="soft" points="210,0 310,0 310,6 222,20"/>
      <rect class="accent" x="293" y="20" width="7" height="7"/>
      <rect class="accent" x="293" y="32" width="7" height="7"/>
      <rect class="accent" x="294" y="120" width="16" height="20"/>
      <circle class="soft" cx="304" cy="196" r="32" role="img" aria-label="Blattzeichnung auf farbiger Scheibe"/>
      <rect class="accent" x="200" y="222" width="34" height="14"/>
    </svg>
    <div class="content">
      <h2 class="product">After Shave Balsam</h2>
      <p class="scent">Orange</p>
      <p class="maker">Hergestellt für Tobias Kranzler e.K.<br>von greenpines, Lindenhofweg 27, 83109 Rosenheim.</p>
      <p class="ingredients"><strong>Ingredients:</strong>Aqua, Stearic Acid, Cocos Nucifera oil, Glycerin, Potassium Hydroxide, Litsea Cubeba oil, (and) Citrus Sinensis Peel oil, Orbignya Oleifera oil, Sodium Hydroxide, Macadamia ternifolia oil, Talc, Kaolin, Citric Acid, Simmondsia chinensis oil, Maris sal, C.I. 77892 (and) Rad Clay, Citral, Limonene, Linalool, Geraniol.</p>
      <p class="volume">60 ml/2.03 FL.OZ.</p>
    </div>
  </section>

  <section class="label peach front">
    <svg class="decor" viewBox="0 0 310 250">
      <circle class="mid" cx="4" cy="38" r="44" role="img" aria-label="Blattzeichnung auf farbiger Scheibe"/>
      <circle class="soft" cx="0" cy="150" r="40"/>
      <rect class="mid" x="0" y="182" width="34" height="26"/>
      <polygon class="soft" points="215,0 310,0 310,6 225,22"/>
      <rect class="mid" x="289" y="24" width="8" height="8"/>
      <rect class="mid" x="289" y="38" width="8" height="8"/>
      <rect class="mid" x="288" y="100" width="22" height="22"/>
      <circle class="soft" cx="296" cy="168" r="46" role="img" aria-label="Blattzeichnung auf farbiger Scheibe"/>
      <rect class="mid" x="248" y="215" width="36" height="18"/>
    </svg>
    <div class="content">
      <p class="brand">Miravel</p>
      <h2 class="product">After Shave Balsam</h2>
      <p class="scent">Pfirsich</p>
      <p class="volume">60 ml/2.03 FL.OZ.</p>
    </div>
  </section>
  <section class="label peach back">
    <svg class="decor" viewBox="0 0 310 250">
      <circle class="mid" cx="4" cy="30" r="36" role="img" aria-label="Blattzeichnung auf farbiger Scheibe"/>
      <circle class="soft" cx="0" cy="160" r="30"/>
      <rect class="mid" x="0" y="200" width="30" height="22"/>
      <polygon class="soft" points="210,0 310,0 310,6 222,20"/>
      <rect class="mid" x="293" y="20" width="7" height="7"/>
      <rect class="mid" x="293" y="32" width="7" height="7"/>
      <rect class="mid" x="294" y="120" width="16" height="20"/>
      <circle class="soft" cx="304" cy="196" r="32" role="img" aria-label="Blattzeichnung auf farbiger Scheibe"/>
      <rect class="mid" x="200" y="222" width="34" height="14"/>
    </svg>
    <div class="content">
      <h2 class="product">After Shave Balsam</h2>
      <p class="scent">Pfirsich</p>
      <p class="maker">Hergestellt für Tobias Kranzler e.K.<br>von greenpines, Lindenhofweg 27, 83109 Rosenheim.</p>
      <p class="ingredients"><strong>Ingredients:</strong>Aqua, Stearic Acid, Cocos Nucifera oil, Glycerin, Potassium Hydroxide, Litsea Cubeba oil, (and) Citrus Sinensis Peel oil, Orbignya Oleifera oil, Sodium Hydroxide, Macadamia ternifolia oil, Talc, Kaolin, Citric Acid, Simmondsia chinensis oil, Maris sal, C.I. 77892 (and) Rad Clay, Citral, Limonene, Linalool, Geraniol.</p>
      <p class="volume">60 ml/2.03 FL.OZ.</p>
    </div>
  </section>

</main>
</body>
</html>
```